Building Design company needing a letterhead

We need a letter head for our Building Design company to send letters etc. to our clients, consultants, councils etc. We would like to see our logo used and company colours. I have attached our style guide and an example of our current letterheads. Top left we would like our logo, top right we would like the company details and at the footer we would like some sort of image/design etc. that suits our brand. I like the Quarto Design letterhead attached.

Target Market(s)

Professionals, Councils, Consultants, Mums & Dads

Industry/Entity Type

Architecture

Font styles to use
Other font styles liked:
• refer the design style guide

Colors
f37122
000000
1b1b1b

Requirements
Must have
• Must have the minimum of a logo, company details and footer
Nice to have
• An image/design made for the footer that would suite our brand and website at www.tavorendesign.com.au. Also it would be nice to include the KMOTR logo somewhere perhaps included in the footer.
Should not have
• Large images in the header. I just want the logo and company details.

```html
<!DOCTYPE html>
<html lang="en">
<head>
<meta charset="utf-8">
<title>Tavoren Design — Letterhead</title>
<link href="https://fonts.googleapis.com/css2?family=Open+Sans:wght@400;600;700&display=swap" rel="stylesheet">
<style>
  :root {
    --brand-orange: #f37122;
    --brand-orange-deep: #e65a22;
    --ink: #1b1b1b;
    --ink-soft: #3a3a3a;
    --rule: #dcdcdc;
    --ghost: #ececec;
    --paper: #ffffff;
  }
  * { margin: 0; padding: 0; box-sizing: border-box; }
  html, body { width: 847px; height: 1200px; overflow: hidden; background: var(--paper); }
  body { font-family: "Open Sans", Arial, sans-serif; color: var(--ink); }

  .letterhead { position: relative; width: 847px; height: 1200px; overflow: hidden; background: var(--paper); }

  .masthead { position: absolute; top: 0; left: 0; right: 0; height: 133px; border-bottom: 1px solid var(--rule); }

  .brand { position: absolute; left: 45px; top: 28px; display: flex; align-items: center; gap: 14px; }
  .brand-square { width: 38px; height: 38px; background: var(--brand-orange); }
  .brand-name {
    font-weight: 700; font-size: 34px; line-height: 38px; letter-spacing: 1.5px;
    text-transform: uppercase; color: var(--ink);
  }

  .sender { position: absolute; right: 39px; top: 50px; text-align: right; }
  .sender-name { font-size: 13px; font-weight: 600; color: var(--brand-orange-deep); text-transform: uppercase; letter-spacing: 0.2px; }
  .sender-role { font-size: 10.5px; color: var(--ink-soft); margin-top: 1px; }

  .backdrop-mark {
    position: absolute; left: 190px; top: 560px; transform: rotate(-27deg); transform-origin: left top;
    font-weight: 700; font-size: 96px; line-height: 100px; letter-spacing: 4px;
    color: var(--ghost); text-transform: uppercase; white-space: nowrap;
  }

  .footer-wave { position: absolute; left: 0; bottom: 0; width: 847px; height: 200px; }

  .footer-address { position: absolute; left: 45px; top: 1157px; font-size: 11.5px; color: #fff; }

  .footer-contacts { position: absolute; right: 39px; top: 1104px; list-style: none; text-align: right; }
  .footer-contacts li {
    display: flex; justify-content: flex-end; align-items: center; gap: 6px;
    font-size: 11.5px; line-height: 17px; color: #fff;
  }
  .footer-contacts svg { width: 11px; height: 11px; fill: #fff; }
</style>
</head>
<body>
<main class="letterhead">
  <header class="masthead">
    <div class="brand">
      <span class="brand-square"></span>
      <span class="brand-name">Tavoren<br>Design</span>
    </div>
    <div class="sender">
      <p class="sender-name">Ellis Marlow</p>
      <p class="sender-role">Trial Attorney</p>
    </div>
  </header>

  <div class="backdrop-mark" aria-hidden="true">Tavoren<br>Design</div>

  <svg class="footer-wave" viewBox="0 0 847 200" preserveAspectRatio="none" aria-hidden="true">
    <defs>
      <linearGradient id="footerFill" x1="1" y1="0" x2="0.6" y2="1">
        <stop offset="0" stop-color="#e4572a"/>
        <stop offset="1" stop-color="#ee7a44"/>
      </linearGradient>
    </defs>
    <path d="M0 122 C 330 128, 650 95, 847 1 L 847 200 L 0 200 Z" fill="url(#footerFill)"/>
  </svg>

  <p class="footer-address">Address Line1, Addres Line2 Country -123456</p>

  <ul class="footer-contacts">
    <li>123-456-7890
      <svg viewBox="0 0 12 12"><path d="M1 4 C1 2 3 1 6 1 C9 1 11 2 11 4 L9 5 L8 3.5 L4 3.5 L3 5 Z M3 6 L9 6 L10 11 L2 11 Z"/></svg>
    </li>
    <li>123-456-7890
      <svg viewBox="0 0 12 12"><path d="M3 1 H8 V4 H3 Z M1 4.5 H11 V11 H1 Z" /><rect x="3" y="6.5" width="6" height="1" fill="#e96a35"/></svg>
    </li>
    <li>info@companyname.com
      <svg viewBox="0 0 12 12"><path d="M1 3 H11 V10 H1 Z"/><path d="M1 3 L6 7 L11 3" stroke="#e96a35" stroke-width="1" fill="none"/></svg>
    </li>
    <li>www.companyname.com
      <svg viewBox="0 0 12 12"><path d="M5 7 L7 5 M4.5 5.5 L2.5 7.5 A1.8 1.8 0 0 0 4.5 9.5 L6.5 7.5 M7.5 6.5 L9.5 4.5 A1.8 1.8 0 0 0 7.5 2.5 L5.5 4.5" stroke="#fff" stroke-width="1.2" fill="none" stroke-linecap="round"/></svg>
    </li>
  </ul>
</main>
</body>
</html>
```